Stationery Design Project for a consulting/educational company

We need a stationery design for a consulting / educational company called "VORT d.o.o.". We are an official partner (yet stand-alone company) of the MELQ Institute, Germany (www.melq-example.de) that covers practically all themes regarding production optimisation, efectiveness, productivity (time studies, workplace organisation,...) We need the design for:

- a CERTIFICATE for seminar participates
- business cards
- letterhead

We are changing our webpage to their design, so we need to change the stationaries as well. I included 2 current logos, one with current color scheme (not important) and the other black/white with a frame. I also included the MELQ original certificate. Only the font + name"VORT" is important, the rest is up to you
Updates

Designs look good, but perhaps a gray & green combo would look nicer? Like on www.melq-example.de? And without the frames?

Target Market(s)

Larger production companies top and middle management

Industry/Entity Type

Business

Requirements
Must have
• - the stationaries (all of them) should, besides the company name "VORT", also include the logo MELQ (in its color), like on their webpage www.melq-example.de
Nice to have
• - certificate could use 5th color (e.g. silver) to make an impression
- similar color scheme to www.melq-example.de

```html
<!DOCTYPE html>
<html lang="en">
<head>
<meta charset="utf-8">
<title>VORT d.o.o. – Stationery</title>
<link rel="stylesheet" href="https://fonts.googleapis.com/css2?family=Open+Sans:wght@400;600;700;800&family=Great+Vibes&display=swap">
<style>
  :root {
    --teal: #1a9aa0;
    --ink: #4d4f52;
    --ink-soft: #6b6d70;
    --logo-grey: #55575a;
    --paper: #ffffff;
    --backdrop: #e9e9ea;
  }
  * { margin: 0; padding: 0; box-sizing: border-box; }
  html, body { width: 1200px; height: 706px; overflow: hidden; }
  body {
    position: relative;
    background: var(--backdrop);
    font-family: "Open Sans", Arial, sans-serif;
    color: var(--ink);
  }
  .sheet {
    position: absolute;
    background: var(--paper);
    box-shadow: 0 2px 8px rgba(0,0,0,.12);
    overflow: hidden;
  }
  .band { position: absolute; background: var(--teal); }
  .wordmark {
    position: absolute;
    font-weight: 800;
    letter-spacing: .04em;
    line-height: 1;
    color: var(--logo-grey);
  }
  .partner-mark {
    position: absolute;
    font-weight: 800;
    letter-spacing: .05em;
    line-height: 1;
    color: var(--logo-grey);
  }

  /* Letterhead */
  .letterhead { left: 650px; top: 21px; width: 470px; height: 664px; }
  .letterhead .wordmark { top: 40px; right: 72px; font-size: 30px; }
  .letterhead .partner-mark { top: 92px; right: 22px; font-size: 20px; }
  .letterhead .band-top { top: 116px; left: 292px; right: 0; height: 10px; }
  .letter-body {
    position: absolute; left: 48px; top: 128px; width: 340px;
    font-size: 7.4px; line-height: 1.5; color: var(--ink-soft);
  }
  .letter-body .salutation { font-weight: 700; color: var(--ink); font-size: 7.8px; margin-bottom: 7px; }
  .letter-body p { margin-bottom: 7px; text-indent: 12px; }
  .signature {
    position: absolute; left: 52px; top: 372px;
    font-family: "Great Vibes", cursive; font-size: 26px; color: var(--ink);
  }
  .signatory-role {
    position: absolute; left: 52px; top: 404px;
    font-size: 7.4px; font-weight: 700; color: var(--ink-soft);
  }
  .letterhead .band-foot { top: 540px; left: 0; width: 290px; height: 11px; }
  .letterhead .contact { left: 302px; top: 566px; }
  .letterhead .corner-tab { top: 628px; right: 0; width: 54px; height: 12px; }

  /* Contact block (shared) */
  .contact { position: absolute; font-size: 7.2px; line-height: 1.45; color: var(--ink-soft); }
  .contact-line { display: flex; align-items: center; gap: 5px; }
  .contact-line svg { width: 8px; height: 8px; flex: none; }
  .contact .web { margin-top: 3px; font-weight: 700; letter-spacing: .22em; color: var(--ink); }

  /* Business cards */
  .card-front { left: 84px; top: 112px; width: 300px; height: 175px; }
  .card-front .wordmark { left: 58px; top: 42px; font-size: 44px; color: var(--teal); }
  .card-front .band { left: 0; right: 0; top: 108px; height: 16px; }

  .card-back { left: 84px; top: 404px; width: 300px; height: 175px; }
  .card-back .person { position: absolute; left: 22px; top: 20px; }
  .card-back .person-name { font-size: 11px; color: var(--ink); }
  .card-back .person-role { font-size: 7px; color: var(--ink-soft); }
  .card-back .contact { left: 22px; top: 52px; font-size: 6.6px; }
  .card-back .wordmark { right: 30px; top: 52px; font-size: 24px; }
  .card-back .partner-mark { right: 26px; top: 92px; font-size: 18px; }
  .card-back .band-main { left: 120px; right: 0; top: 114px; height: 14px; }
  .card-back .band-tab { left: 0; top: 124px; width: 10px; height: 12px; }
</style>
</head>
<body>

<svg width="0" height="0" style="position:absolute" aria-hidden="true">
  <defs>
    <symbol id="icon-phone" viewBox="0 0 10 10"><rect width="10" height="10" rx="1" fill="#1a9aa0"/><path d="M3 2h1.4l.6 1.6-.9.6a4 4 0 0 0 1.7 1.7l.6-.9L8 5.6V7a1 1 0 0 1-1 1A5 5 0 0 1 2 3a1 1 0 0 1 1-1z" fill="#fff"/></symbol>
    <symbol id="icon-fax" viewBox="0 0 10 10"><rect width="10" height="10" rx="1" fill="#1a9aa0"/><rect x="2" y="4" width="6" height="4" fill="#fff"/><rect x="3" y="2" width="4" height="2" fill="#fff"/></symbol>
    <symbol id="icon-mail" viewBox="0 0 10 10"><rect width="10" height="10" rx="1" fill="#1a9aa0"/><rect x="2" y="3" width="6" height="4.4" fill="#fff"/><path d="M2 3l3 2.4L8 3" stroke="#1a9aa0" stroke-width=".8" fill="none"/></symbol>
  </defs>
</svg>

<!-- Business card, front -->
<div class="sheet card-front">
  <div class="wordmark">VORT</div>
  <div class="band"></div>
</div>

<!-- Business card, back -->
<div class="sheet card-back">
  <div class="person">
    <div class="person-name">Name Surname</div>
    <div class="person-role">Operation Manager</div>
  </div>
  <div class="contact">
    <div class="contact-line"><svg><use href="#icon-phone"/></svg>(000) 55 010 20 30</div>
    <div class="contact-line"><svg><use href="#icon-fax"/></svg>(000) 55 010 20 31</div>
    <div class="contact-line"><svg><use href="#icon-mail"/></svg>name@vort-example.com</div>
    <div style="margin-top:4px">Avenue Example 12 - Midtown</div>
    <div>PO 100 - City, Country</div>
    <div class="web" style="letter-spacing:.05em">www.vort-example.com</div>
  </div>
  <div class="wordmark">VORT</div>
  <div class="partner-mark">MELQ</div>
  <div class="band band-main"></div>
  <div class="band band-tab"></div>
</div>

<!-- Letterhead -->
<div class="sheet letterhead">
  <div class="wordmark">VORT</div>
  <div class="partner-mark">MELQ</div>
  <div class="band band-top"></div>

  <div class="letter-body">
    <div class="salutation">Lorem Ipsum,</div>
    <p>Cras mattis consectetur purus sit amet fermentum. Etiam porta sem malesuada magna mollis euismod. Integer posuere erat a ante venenatis dapibus posuere velit aliquet. Cras justo odio, dapibus ac facilisis in, egestas eget quam. Aenean eu leo quam. Pellentesque ornare sem lacinia quam venenatis vestibulum.</p>
    <p>Vivamus sagittis lacus vel augue laoreet rutrum faucibus dolor auctor. Donec sed odio dui. Etiam porta sem malesuada magna mollis euismod. Morbi leo risus, porta ac consectetur ac, vestibulum at eros. Nullam id dolor id nibh ultricies vehicula ut id elit.</p>
    <p>Donec id elit non mi porta gravida at eget metus. Fusce dapibus, tellus ac cursus commodo, tortor mauris condimentum nibh, ut fermentum massa justo sit amet risus. Cras justo odio, dapibus ac facilisis in, egestas eget quam. Cum sociis natoque penatibus et magnis dis parturient montes, nascetur ridiculus mus.</p>
    <p>Cum sociis natoque penatibus et magnis dis parturient montes, nascetur ridiculus mus. Curabitur blandit tempus porttitor. Aenean lacinia bibendum nulla sed consectetur. Lorem ipsum dolor sit amet, consectetur adipiscing elit.</p>
    <p>Cras justo odio, dapibus ac facilisis in, egestas eget quam. Morbi leo risus, porta ac consectetur ac, vestibulum at eros. Duis mollis, est non commodo luctus, nisi erat porttitor ligula, eget lacinia odio sem nec elit. Integer posuere erat a ante venenatis dapibus posuere velit aliquet. Vivamus sagittis lacus vel augue laoreet rutrum faucibus dolor auctor.</p>
  </div>

  <div class="signature">Your Name</div>
  <div class="signatory-role">Company Director</div>

  <div class="band band-foot"></div>
  <div class="contact">
    <div class="contact-line"><svg><use href="#icon-phone"/></svg>(000) 55 010 20 30</div>
    <div class="contact-line"><svg><use href="#icon-fax"/></svg>(000) 55 010 20 31</div>
    <div class="contact-line"><svg><use href="#icon-mail"/></svg>name@vort-example.com</div>
    <div>Avenue Example 12 - Midtown</div>
    <div>PO 100 - City, Country</div>
    <div class="web">www.vort-example.com</div>
  </div>
  <div class="band corner-tab"></div>
</div>

</body>
</html>
```